Brightvale Fire Solutions business card, logo and web design.

We need business cards for our new company. We are based in South Africa. We specialise in fire detection, fire prevention, security, access control and CCTV in buildings. We service and install sprinkler systems, fire hose reals and fire extinguishers in buildings. Our slogan in the company is "Compliance is our business" . We strive to be innovators in our field and deliver the best service possible at the best quality. We want to be the best in our field. We don't have any colour preferences as long as it relates to our type of business.
Our target market is clients that owns big buildings with multiple levels, such a malls,office buildings or warehouses.

Target Market(s)

Industry/Entity Type

Fire Safety

Contact Information for Business Card

The front of the card should have the company name (Brightvale Fire Solutions (PTY) LTD. and a description of the company. Fire engineering & security services.

Logo Text

Compliance is our business

Number of Pages Required

4 page

Font styles to use
Serif

Colors

Designer to choose colors to be used in the design.

Requirements
Must have
• The company name, the logo and all the details on the back of the card. It should be simple and not to busy.
Nice to have
• Just something different and new. Brightvale means - innovate so the card should represent our name.
Should not have
• Small pictures or lots of graphics on.

```html
<!DOCTYPE html>
<html lang="en">
<head>
<meta charset="utf-8">
<title>Brightvale Fire Solutions – Business Card</title>
<link rel="stylesheet" href="https://fonts.googleapis.com/css2?family=Russo+One&family=Saira+Condensed:wght@400;500;600&display=swap">
<style>
  :root {
    --bg: #6fcab6;
    --blue-bright: #0a14f0;
    --blue-deep: #000a7a;
    --navy: #000659;
    --band-grey: #cfcfcf;
    --title-grey: #dcdcdc;
    --wash-grey: #e8e8e8;
    --ink-navy: #0a0a6e;
    --white: #ffffff;
    --shadow-grey: #a9a9ad;
  }
  html, body {
    margin: 0;
    padding: 0;
    width: 925px;
    height: 1200px;
    overflow: hidden;
    background: var(--bg);
  }
  .canvas {
    position: relative;
    width: 925px;
    height: 1200px;
  }
  .card {
    position: absolute;
    left: 112px;
    width: 700px;
    height: 400px;
    overflow: hidden;
    box-shadow: 0 6px 18px rgba(0, 40, 40, 0.25);
  }
  .card--front { top: 150px; background: linear-gradient(180deg, var(--blue-bright) 0%, var(--blue-deep) 72%); }
  .card--back { top: 660px; background: var(--white); }

  /* Front */
  .front__name {
    position: absolute; left: 0; right: 0; top: 108px;
    text-align: center;
    font-family: "Russo One", sans-serif;
    font-size: 72px; letter-spacing: 1px;
    color: var(--title-grey);
    line-height: 1;
  }
  .front__sub {
    position: absolute; left: 0; right: 0; top: 198px;
    text-align: center;
    color: var(--title-grey);
    font-size: 30px;
    line-height: 1;
  }
  .front__sub .bold { font-family: "Russo One", sans-serif; font-size: 28px; }
  .front__sub .light { font-family: "Saira Condensed", sans-serif; font-weight: 400; font-size: 32px; }
  .front__band {
    position: absolute; left: 0; right: 0; top: 290px; height: 36px;
    background: var(--band-grey);
    font-family: "Saira Condensed", sans-serif; font-weight: 500;
    font-size: 29px; line-height: 36px; color: #111;
    text-align: center; letter-spacing: 0.2px;
  }
  .front__base {
    position: absolute; left: 0; right: 0; top: 326px; bottom: 0;
    background: var(--navy);
  }

  /* Back */
  .back__shapes { position: absolute; inset: 0; }
  .back__fields {
    position: absolute; left: 30px; top: 30px;
    font-family: "Saira Condensed", sans-serif; font-weight: 500;
    font-size: 31px; line-height: 42px; color: var(--ink-navy);
  }
  .back__reg {
    position: absolute; right: 22px; top: 28px; width: 175px;
    text-align: center;
    font-family: "Saira Condensed", sans-serif; font-weight: 400;
    font-size: 22px; line-height: 31px; color: var(--white);
  }
  .back__wash-name {
    position: absolute; left: 0; right: 0; top: 218px;
    text-align: center;
    font-family: "Russo One", sans-serif;
    font-size: 64px; line-height: 1; color: var(--wash-grey);
  }
  .back__wash-sub {
    position: absolute; left: 0; right: 0; top: 291px;
    text-align: center;
    font-family: "Russo One", sans-serif;
    font-size: 26px; line-height: 1; color: var(--wash-grey);
  }
  .back__contact {
    position: absolute; left: 118px; top: 330px;
    font-family: "Saira Condensed", sans-serif; font-weight: 500;
    font-size: 22px; line-height: 30px; color: var(--ink-navy);
  }
  .back__contact .fax { position: absolute; left: 305px; top: 0; }
</style>
</head>
<body>
<main class="canvas">

  <section class="card card--front" aria-label="Business card front">
    <div class="front__name">BRIGHTVALE</div>
    <div class="front__sub"><span class="bold">Fire Solutions</span> <span class="light">(PTY) LTD</span></div>
    <div class="front__band">FIRE ENGINEERING &amp; SECURITY SERVICES</div>
    <div class="front__base"></div>
  </section>

  <section class="card card--back" aria-label="Business card back">
    <svg class="back__shapes" width="700" height="400" viewBox="0 0 700 400" aria-hidden="true">
      <defs>
        <linearGradient id="panelBlue" x1="0" y1="0" x2="0" y2="1">
          <stop offset="0" stop-color="#000a66"/>
          <stop offset="1" stop-color="#0a18f2"/>
        </linearGradient>
      </defs>
      <polygon points="468,0 487,0 487,140 700,198 700,218 482,160" fill="var(--shadow-grey)"/>
      <polygon points="487,0 700,0 700,198 487,140" fill="url(#panelBlue)"/>
      <polygon points="0,318 88,332 88,400 0,400" fill="url(#panelBlue)"/>
    </svg>
    <div class="back__fields">Name:<br>Cell:<br>Email:</div>
    <div class="back__reg">Company VAT:<br>4120098765<br>Company Reg:<br>08/245113/07</div>
    <div class="back__wash-name">BRIGHTVALE</div>
    <div class="back__wash-sub">Fire Solutions (PTY) LTD</div>
    <div class="back__contact">
      Telephone:<span class="fax">Fax:</span><br>
      Address: 14 Larkspur Avenue. Hillcrest Park. Pretoria. 0190
    </div>
  </section>

</main>
</body>
</html>
```